Brellix Systems Banner Stand Design

Looking for a banner stand design that is ready to print for an upcoming trade show. 33"x82" are the dimensions. It will need to catch the eye of those walking by our booth with a very generic description/bullet points of what/who we are. As a technology firm we like our printed material to be very crisp and new age as to say, we are are the forefront of our business.

Please refer to the attachments for more info.

Target Market(s)

Technical trade show attendees

Industry/Entity Type

Trade

Font styles to use
Sans Serif

Requirements
Must have
• Must have our logo, the majority of the design should be graphics, with 1/3 content that we will include, but it should consist of a sentence or two with about 8 bullet points. I have included our logo and our one-pager which will be printed and used in conjunction with the banner stand.
Nice to have
• As a tech firm that provides cloud and managed services we would like the graphics to be advanced so show that we are always keeping up with the ever growing tech field but that we also keep our customer as our main priority.
Should not have
• Should not have much room for content, we want to be able to use this at any event

```html
<!DOCTYPE html>
<html lang="en">
<head>
<meta charset="utf-8">
<title>Brellix Systems Banner Stand</title>
<link href="https://fonts.googleapis.com/css2?family=Oswald:wght@400;700&display=swap" rel="stylesheet">
<style>
  :root {
    --navy: #0d3a4f;
    --white: #ffffff;
    --blue-a: #22b3e8;
    --blue-b: #0a8ad2;
    --orange-a: #f29448;
    --orange-b: #dd5f0c;
    --green-a: #d8e7a8;
    --green-b: #86bb36;
    --red-a: #ea5a44;
    --red-b: #c80f1a;
  }
  html, body {
    margin: 0;
    padding: 0;
    width: 1200px;
    height: 4468px;
    overflow: hidden;
    background: var(--navy);
  }
  .banner {
    position: relative;
    width: 1200px;
    height: 4468px;
    background: var(--navy);
    font-family: "Oswald", sans-serif;
  }
  .brand {
    position: absolute;
    left: 168px;
    top: 560px;
    display: flex;
    align-items: center;
    gap: 40px;
  }
  .brand-mark {
    width: 132px;
    height: 132px;
    background: var(--orange-b);
  }
  .brand-name {
    color: var(--white);
    font-weight: 400;
    font-size: 100px;
    line-height: 1;
    letter-spacing: 2px;
    white-space: nowrap;
  }
  .steps {
    position: absolute;
    left: 0;
    top: 0;
  }
  .step-number {
    font-family: "Oswald", sans-serif;
    font-weight: 700;
    font-size: 84px;
    fill: var(--white);
  }
</style>
</head>
<body>
<div class="banner">
  <div class="brand">
    <div class="brand-mark"></div>
    <div class="brand-name">Brellix Systems</div>
  </div>

  <svg class="steps" width="1200" height="4468" viewBox="0 0 1200 4468" xmlns="http://www.w3.org/2000/svg">
    <defs>
      <linearGradient id="grad-blue" x1="0" x2="1" y1="0" y2="0">
        <stop offset="0" stop-color="var(--blue-a)"/><stop offset="1" stop-color="var(--blue-b)"/>
      </linearGradient>
      <linearGradient id="grad-orange" x1="0" x2="1" y1="0" y2="0">
        <stop offset="0" stop-color="var(--orange-a)"/><stop offset="1" stop-color="var(--orange-b)"/>
      </linearGradient>
      <linearGradient id="grad-green" x1="0" x2="1" y1="0" y2="0">
        <stop offset="0" stop-color="var(--green-a)"/><stop offset="1" stop-color="var(--green-b)"/>
      </linearGradient>
      <linearGradient id="grad-red" x1="0" x2="1" y1="0" y2="0">
        <stop offset="0" stop-color="var(--red-a)"/><stop offset="0.5" stop-color="#e0101a"/><stop offset="1" stop-color="var(--red-b)"/>
      </linearGradient>
      <g id="step-arrow">
        <path d="M0 24 H150 V0 L222 120 L150 240 V216 H0 Z"/>
      </g>
      <g id="step-ribbon">
        <path d="M0 0 H800 L712 120 L800 240 H0 Z"/>
      </g>
    </defs>

    <g class="step" transform="translate(0 1168)">
      <use href="#step-arrow" fill="url(#grad-blue)"/>
      <use href="#step-ribbon" x="320" fill="url(#grad-blue)"/>
      <text class="step-number" x="112" y="150" text-anchor="middle">1</text>
    </g>
    <g class="step" transform="translate(0 1436)">
      <use href="#step-arrow" fill="url(#grad-orange)"/>
      <use href="#step-ribbon" x="320" fill="url(#grad-orange)"/>
      <text class="step-number" x="112" y="150" text-anchor="middle">2</text>
    </g>
    <g class="step" transform="translate(0 1704)">
      <use href="#step-arrow" fill="url(#grad-green)"/>
      <use href="#step-ribbon" x="320" fill="url(#grad-green)"/>
      <text class="step-number" x="112" y="150" text-anchor="middle">3</text>
    </g>
    <g class="step" transform="translate(0 1972)">
      <use href="#step-arrow" fill="url(#grad-red)"/>
      <use href="#step-ribbon" x="320" fill="url(#grad-red)"/>
      <text class="step-number" x="112" y="150" text-anchor="middle">4</text>
    </g>
    <g class="step" transform="translate(0 2240)">
      <use href="#step-arrow" fill="url(#grad-blue)"/>
      <use href="#step-ribbon" x="320" fill="url(#grad-blue)"/>
      <text class="step-number" x="112" y="150" text-anchor="middle">5</text>
    </g>
    <g class="step" transform="translate(0 2508)">
      <use href="#step-arrow" fill="url(#grad-orange)"/>
      <use href="#step-ribbon" x="320" fill="url(#grad-orange)"/>
      <text class="step-number" x="112" y="150" text-anchor="middle">6</text>
    </g>
    <g class="step" transform="translate(0 2776)">
      <use href="#step-arrow" fill="url(#grad-green)"/>
      <use href="#step-ribbon" x="320" fill="url(#grad-green)"/>
      <text class="step-number" x="112" y="150" text-anchor="middle">7</text>
    </g>
    <g class="step" transform="translate(0 3044)">
      <use href="#step-arrow" fill="url(#grad-red)"/>
      <use href="#step-ribbon" x="320" fill="url(#grad-red)"/>
      <text class="step-number" x="112" y="150" text-anchor="middle">8</text>
    </g>
  </svg>
</div>
</body>
</html>
```